Flyer for Pharmacy/Medical Convention

Tri-fold flyer for pharmacy/medical convention. The inside of the flyer we would like to look like a venn diagram, possibly using an image similar to our blue logo

Copy write will be submitted when a design is chosen

there will be a flap about educational features, one about supplements an automated recommendations, and a flap about a computer platform to manage patients

Target Market(s)

Pharmacists and Medical Providers

Industry/Entity Type

Supplement

Colors

Designer to choose colors to be used in the design.

Requirements
Must have
• color scheme similar to logos and or label design attached

```html
<!DOCTYPE html>
<html lang="en">
<head>
<meta charset="utf-8">
<title>Veridane Wellness – Tri-fold Flyer</title>
<link href="https://fonts.googleapis.com/css2?family=Roboto+Condensed:wght@400;700&family=Roboto:wght@400;500;700&display=swap" rel="stylesheet">
<style>
:root{
  --navy:#1d2484;
  --blue:#2443ad;
  --royal:#2f5bd0;
  --dark:#2c2d33;
  --ink:#3a3d4a;
  --muted:#6b6f7c;
  --light:#f3f3f6;
  --lavender:#dfe0ea;
  --yellow:#f4e21a;
  --white:#ffffff;
  --stage:#e4e5ea;
}
*{box-sizing:border-box;margin:0;padding:0}
html,body{width:1200px;height:900px;overflow:hidden;background:var(--stage);font-family:"Roboto",Arial,sans-serif;color:var(--ink)}
.canvas{position:relative;width:1200px;height:900px}
.spread{position:absolute;left:30px;width:1140px;height:420px;display:flex;box-shadow:0 6px 18px rgba(20,25,60,.18)}
.spread--outside{top:20px}
.spread--inside{top:460px}
.panel{position:relative;width:380px;height:420px;overflow:hidden;background:var(--white)}
.panel svg.bg{position:absolute;inset:0;width:380px;height:420px}
.abs{position:absolute}
.heading{font-family:"Roboto Condensed",Arial,sans-serif;color:var(--navy);font-weight:700;text-transform:uppercase;line-height:1}
.subheading{font-family:"Roboto Condensed",Arial,sans-serif;font-weight:400;text-transform:uppercase;font-size:12px;color:var(--navy)}
.rule{width:34px;height:2px;background:var(--navy);margin:5px 0 7px}
.body-copy{font-size:8px;line-height:1.35;color:var(--muted)}
.bullets{list-style:none}
.bullets li{position:relative;padding-left:12px;font-size:8px;line-height:1.35;margin-bottom:9px}
.bullets li::before{content:"";position:absolute;left:0;top:3px;width:4px;height:4px;background:currentColor}
.brand{display:flex;align-items:center;gap:7px;font-family:"Roboto Condensed",Arial,sans-serif;font-weight:700;font-size:17px;color:var(--navy);letter-spacing:.5px;text-transform:uppercase}
.brand::before{content:"";width:12px;height:12px;border-radius:50%;background:var(--navy)}
.web{font-family:"Roboto",Arial,sans-serif;font-size:8px;color:#d8d9e0;letter-spacing:.3px}
.cta-small{font-family:"Roboto Condensed",Arial,sans-serif;font-size:22px;color:var(--navy)}
.cta-big{font-family:"Roboto Condensed",Arial,sans-serif;font-weight:700;font-size:32px;color:var(--navy)}
.cta-sub{font-size:11px;color:var(--muted)}
.cta-steps{font-family:"Roboto Condensed",Arial,sans-serif;font-weight:700;font-size:22px;color:var(--navy)}
.tiny{font-size:7px;color:var(--muted);line-height:1.3}
.contact{text-align:center;font-size:7.5px;color:var(--ink);line-height:1.3}
.contact svg{display:block;margin:0 auto 3px}
.feature{display:flex;gap:9px;align-items:flex-start}
.feature h4{font-size:10px;color:var(--navy);font-weight:700;border-bottom:1px solid var(--navy);display:inline-block;margin-bottom:3px}
.feature p{font-size:7.5px;line-height:1.3;color:var(--muted)}
.icon-disc{flex:none;width:24px;height:24px;border-radius:50%;background:var(--blue);display:flex;align-items:center;justify-content:center}
.white{color:var(--white)}
</style>
</head>
<body>
<main class="canvas">

  <section class="spread spread--outside" aria-label="Flyer outside">

    <article class="panel panel--platform">
      <svg class="bg" viewBox="0 0 380 420" aria-hidden="true">
        <defs>
          <linearGradient id="couplePhoto" x1="0" y1="0" x2="1" y2="1">
            <stop offset="0" stop-color="#c9d4dc"/><stop offset=".5" stop-color="#d9b9a0"/><stop offset="1" stop-color="#8d98a8"/>
          </linearGradient>
        </defs>
        <path d="M0 150 C120 140 200 160 260 190 L380 260 L380 420 L0 420Z" fill="var(--navy)"/>
        <path d="M0 165 C110 158 190 175 245 205 L380 285 L380 420 L0 420Z" fill="var(--dark)"/>
      </svg>
      <svg class="abs" style="left:0;top:0" width="380" height="420" viewBox="0 0 380 420">
        <path role="img" aria-label="Photo of a smiling mature couple" d="M0 260 C60 240 150 240 200 290 C225 320 230 380 222 420 L0 420Z" fill="url(#couplePhoto)"/>
        <path d="M200 290 C225 320 230 380 222 420" stroke="var(--blue)" stroke-width="6" fill="none"/>
      </svg>
      <div class="abs" style="left:22px;top:24px;width:190px">
        <div class="heading" style="font-size:15px;text-transform:none">Computer platform</div>
        <div class="subheading" style="font-size:9px">To manage patients</div>
        <div class="rule"></div>
        <p class="body-copy">Lorem ipsum dolor sit amet, consectetuer adipiscing elit, sed diam nonummy nibh euismod tincidunt ut laoreet dolore magna aliquam erat volutpat.</p>
        <p class="body-copy" style="margin-top:6px;padding-left:8px"><b style="color:var(--navy);text-transform:uppercase">Lorem ipsum</b><br>Lorem ipsum dolor sit amet, consectetuer adipiscing.</p>
      </div>
      <div class="abs" style="left:45px;top:152px;width:136px;height:136px;border-radius:50%;background:var(--white);padding:5px">
        <div style="width:100%;height:100%;border-radius:50%;background:radial-gradient(circle at 40% 35%,var(--royal),var(--navy));border:3px solid var(--blue);display:flex;align-items:center;justify-content:center;text-align:center;font-family:'Roboto Condensed',Arial,sans-serif;font-size:12px;line-height:1.2;color:var(--white)">
          <div><b style="color:var(--yellow)">FILL<br>NUTRITIONAL</b><br>gaps that can<br>lead to a<br><b style="color:var(--yellow)">HORMONE<br>IMBALANCE.</b></div>
        </div>
      </div>
    </article>

    <article class="panel panel--contact">
      <svg class="bg" viewBox="0 0 380 420" aria-hidden="true">
        <path d="M0 250 C80 230 260 230 380 250 L380 420 L0 420Z" fill="var(--dark)"/>
      </svg>
      <div class="abs" style="left:0;right:0;top:38px;display:flex;justify-content:center"><span class="brand">Veridane Wellness</span></div>
      <div class="abs" style="left:0;right:0;top:95px">
        <div class="contact"><svg width="10" height="12" viewBox="0 0 10 12"><path d="M5 11 C2 7 1 5.5 1 4a4 4 0 0 1 8 0c0 1.5-1 3-4 7z" fill="none" stroke="var(--navy)" stroke-width="1.2"/><circle cx="5" cy="4" r="1.3" fill="var(--navy)"/></svg>123 Lorem Ipsum Street,<br>magna aliquam volutpat. 145781</div>
        <div class="contact" style="margin-top:14px"><svg width="10" height="10" viewBox="0 0 10 10"><path d="M2 1 L4 3 L3 4.5 C3.8 6 4.5 6.7 5.5 7 L7 6 L9 8 L7.8 9.3 C4.5 9 1 5.5 0.7 2.2Z" fill="none" stroke="var(--navy)" stroke-width="1"/></svg>+14 5550 0142</div>
        <div class="contact" style="margin-top:14px"><svg width="11" height="9" viewBox="0 0 11 9"><rect x=".5" y=".5" width="10" height="8" fill="none" stroke="var(--navy)"/><path d="M.5 .5 L5.5 5 L10.5 .5" fill="none" stroke="var(--navy)"/></svg>info@veridanewellness.com</div>
      </div>
      <div role="img" aria-label="Photo of golden supplement capsules" class="abs" style="left:24px;top:212px;width:78px;height:78px;border-radius:50%;border:4px solid var(--white);background:radial-gradient(circle at 45% 40%,#f7c64a,#c98a1e 55%,#e9e4dc 56%)"></div>
      <div class="abs" style="left:104px;top:226px;width:160px;height:160px;border-radius:50%;border:5px solid var(--blue);background:var(--white);padding:3px">
        <div role="img" aria-label="Photo of a woman in a hoodie holding a green smoothie" style="width:100%;height:100%;border-radius:50%;background:linear-gradient(160deg,#c7ccd3,#8b8f96 60%,#6b7a5a)"></div>
      </div>
      <div class="abs web" style="left:0;right:0;bottom:10px;text-align:center">www.veridanewellness.com</div>
    </article>

    <article class="panel panel--cover" style="background:linear-gradient(180deg,#f4f4f6,#dcdce2)">
      <svg class="bg" viewBox="0 0 380 420" aria-hidden="true">
        <defs>
          <linearGradient id="sleepPhoto" x1="0" y1="0" x2="1" y2="1"><stop offset="0" stop-color="#ece9e6"/><stop offset=".6" stop-color="#c9b3a4"/><stop offset="1" stop-color="#f4f2ef"/></linearGradient>
          <linearGradient id="swoosh" x1="0" x2="1"><stop offset="0" stop-color="var(--navy)"/><stop offset="1" stop-color="var(--royal)"/></linearGradient>
        </defs>
        <path d="M0 330 C120 365 260 365 380 320 L380 420 L0 420Z" fill="url(#swoosh)"/>
        <path d="M0 362 C120 392 260 392 380 355 L380 420 L0 420Z" fill="var(--dark)"/>
        <path d="M70 0 L380 0 L380 110 C300 110 190 90 130 60 C100 45 80 25 70 0Z" fill="var(--blue)"/>
      </svg>
      <svg class="abs" style="left:0;top:0" width="380" height="420" viewBox="0 0 380 420">
        <path role="img" aria-label="Photo of a woman sleeping peacefully" d="M80 0 L380 0 L380 98 C300 98 200 80 140 50 C110 35 90 18 80 0Z" fill="url(#sleepPhoto)"/>
      </svg>
      <div class="abs" style="left:16px;top:20px;width:48px;height:48px;border-radius:50%;background:radial-gradient(circle at 35% 35%,var(--royal),var(--navy))"></div>
      <div class="abs" style="left:24px;top:126px"><span class="brand" style="font-size:14px">Veridane Wellness</span></div>
      <div class="abs" style="left:24px;top:172px">
        <div class="cta-small">GET YOUR</div>
        <div class="cta-big" style="margin-top:-2px">CUSTOMIZED</div>
        <div class="cta-sub">Supplement Recommendations</div>
        <div class="rule" style="width:60px;margin:6px 0"></div>
        <div class="cta-steps">IN 3 EASY STEPS</div>
        <div class="tiny" style="margin-top:3px">Select Gender | Select Medical Conditions<br>Enter Your Current Medications</div>
      </div>
      <div class="abs web" style="left:0;right:0;bottom:10px;text-align:center">www.veridanewellness.com</div>
    </article>
  </section>

  <section class="spread spread--inside" aria-label="Flyer inside">

    <article class="panel panel--education" style="background:linear-gradient(180deg,var(--lavender),#eeeef3)">
      <svg class="bg" viewBox="0 0 380 420" aria-hidden="true">
        <rect x="0" y="392" width="380" height="28" fill="var(--navy)"/>
      </svg>
      <div class="abs" style="left:22px;top:18px">
        <div class="heading" style="font-size:15px">Educational</div>
        <div class="subheading" style="font-size:14px">Features</div>
      </div>
      <div class="abs" style="left:22px;top:60px;width:340px">
        <div class="feature"><svg width="24" height="18" viewBox="0 0 24 18"><rect x="1" y="3" width="18" height="12" rx="1" fill="none" stroke="var(--navy)" stroke-width="1.4"/><line x1="1" y1="7" x2="19" y2="7" stroke="var(--navy)" stroke-width="2"/></svg><div><h4>Lorem Ipsum</h4><p>Lorem ipsum dolor sit amet, consectetur adipiscing elit, sed do eiusmod tempor incididunt ut.</p></div></div>
        <div class="feature" style="margin-top:10px"><svg width="24" height="18" viewBox="0 0 24 18"><circle cx="10" cy="7" r="5.5" fill="none" stroke="var(--navy)" stroke-width="1.4"/><line x1="8" y1="15" x2="12" y2="15" stroke="var(--navy)" stroke-width="1.4"/></svg><div><h4>Lorem Ipsum</h4><p>Lorem ipsum dolor sit amet, consectetur adipiscing elit, sed do eiusmod tempor incididunt ut.</p></div></div>
      </div>
      <div class="abs" style="left:120px;top:148px;width:136px;height:136px;border-radius:50%;border:5px solid var(--navy);background:var(--white);padding:3px">
        <div role="img" aria-label="Photo of a tired person resting their head on a laptop" style="width:100%;height:100%;border-radius:50%;background:linear-gradient(180deg,#9aa0a8,#d8d8dc 55%,#7d8088)"></div>
      </div>
      <div role="img" aria-label="Photo of a supplement bottle" class="abs" style="left:54px;top:226px;width:56px;height:56px;border-radius:50%;border:3px solid var(--navy);background:radial-gradient(circle,#3a4ca8 30%,#e7e8ee 32%)"></div>
      <div class="abs" style="left:22px;top:296px;width:340px">
        <div class="feature"><svg width="24" height="18" viewBox="0 0 24 18"><path d="M1 1 V17 H22" fill="none" stroke="var(--navy)" stroke-width="1.2"/><path d="M3 14 L9 8 L13 11 L21 4" fill="none" stroke="var(--navy)" stroke-width="1.2"/></svg><div><h4>Lorem Ipsum</h4><p>Lorem ipsum dolor sit amet, consectetur adipiscing elit, sed do eiusmod tempor incididunt ut.</p></div></div>
        <div class="feature" style="margin-top:10px"><svg width="24" height="18" viewBox="0 0 24 18"><path d="M12 2 L5 17 M12 2 L19 17 M7 12 H17" fill="none" stroke="var(--navy)" stroke-width="1.2"/><circle cx="12" cy="3" r="1.6" fill="var(--navy)"/></svg><div><h4>Lorem Ipsum</h4><p>Lorem ipsum dolor sit amet, consectetur adipiscing elit, sed do eiusmod tempor incididunt ut.</p></div></div>
      </div>
      <div class="abs web" style="left:22px;bottom:8px;font-size:9px;color:#aab3e6">www.veridanewellness.com</div>
    </article>

    <article class="panel panel--supplements" style="background:linear-gradient(180deg,#ffffff,#e6e8f0)">
      <svg class="bg" viewBox="0 0 380 420" aria-hidden="true">
        <path d="M0 0 L380 0 L380 250 L150 250 C70 250 0 200 0 120Z" fill="var(--blue)"/>
      </svg>
      <div class="abs white" style="left:24px;top:18px;width:330px">
        <div class="heading white" style="font-size:20px;font-weight:400">LOREM IPSUM</div>
        <div class="subheading white" style="font-size:10px">Place your text here</div>
        <div class="rule" style="background:var(--white)"></div>
        <ul class="bullets" style="margin-top:8px">
          <li>Recognizing a need for a line of nutritional supplements designed by health care professionals, for health care professionals, Veridane Wellness was created.</li>
          <li>Recognizing a need for a line of nutritional supplements designed by health care professionals, for health care professionals, Veridane Wellness was created.</li>
        </ul>
      </div>
      <div class="abs" style="left:20px;top:152px;width:128px;height:128px;border-radius:50%;background:var(--white);border:4px solid var(--navy);display:flex;align-items:center;justify-content:center;text-align:center">
        <div><div class="heading" style="font-size:19px">Research</div><div style="font-size:13px;color:var(--blue);line-height:1.2;margin-top:3px">Based formulas<br>at therapeutic<br>Dosages</div></div>
      </div>
      <div class="abs" style="left:24px;top:290px">
        <div class="heading" style="font-size:12px">Supplements an</div>
        <div class="subheading" style="font-size:9px">Automated recommendations</div>
      </div>
      <div class="abs" style="left:24px;top:318px;width:330px;display:flex;flex-direction:column;gap:4px">
        <div class="feature"><span class="icon-disc"><svg width="12" height="12" viewBox="0 0 12 12"><circle cx="6" cy="4" r="2.3" fill="none" stroke="#fff"/><path d="M1.5 11 C2 7.5 10 7.5 10.5 11" fill="none" stroke="#fff"/></svg></span><div><h4>Lorem Ipsum</h4><p>Lorem ipsum dolor sit amet, consectetuer adipiscing elit.</p></div></div>
        <div class="feature"><span class="icon-disc"><svg width="12" height="12" viewBox="0 0 12 12"><circle cx="5" cy="5" r="3.3" fill="none" stroke="#fff"/><line x1="7.5" y1="7.5" x2="11" y2="11" stroke="#fff"/></svg></span><div><h4>Lorem Ipsum</h4><p>Lorem ipsum dolor sit amet, consectetuer adipiscing elit.</p></div></div>
        <div class="feature"><span class="icon-disc"><svg width="12" height="12" viewBox="0 0 12 12"><path d="M2 10 L10 2 M5 2 H10 V7" fill="none" stroke="#fff"/></svg></span><div><h4>Lorem Ipsum</h4><p>Lorem ipsum dolor sit amet, consectetuer adipiscing elit.</p></div></div>
      </div>
    </article>

    <article class="panel panel--service" style="background:var(--white)">
      <svg class="bg" viewBox="0 0 380 420" aria-hidden="true">
        <defs>
          <linearGradient id="serviceBand" x1="0" y1="0" x2="1" y2="1"><stop offset="0" stop-color="var(--royal)"/><stop offset="1" stop-color="var(--navy)"/></linearGradient>
          <linearGradient id="runnersPhoto" x1="0" y1="0" x2="0" y2="1"><stop offset="0" stop-color="#c9d2c3"/><stop offset=".5" stop-color="#b88f86"/><stop offset="1" stop-color="#5b4a55"/></linearGradient>
        </defs>
        <path d="M0 0 L380 0 L380 140 C330 220 200 260 0 270Z" fill="url(#serviceBand)"/>
      </svg>
      <svg class="abs" style="left:0;top:0" width="380" height="420" viewBox="0 0 380 420">
        <path role="img" aria-label="Photo of a woman and a man jogging outdoors" d="M0 270 C200 260 330 220 380 140 L380 420 L0 420Z" fill="url(#runnersPhoto)"/>
      </svg>
      <div role="img" aria-label="Photo of fresh vegetables and herbs" class="abs" style="right:-20px;top:-20px;width:90px;height:90px;border-radius:50%;border:4px solid var(--white);background:radial-gradient(circle at 40% 55%,#c8432d,#6c8c3a 55%,#8a6a4a)"></div>
      <div class="abs white" style="left:22px;top:18px;width:270px">
        <div class="heading white" style="font-size:15px">Our</div>
        <div class="subheading white" style="font-size:14px">Service</div>
        <div class="rule" style="background:var(--white)"></div>
        <ul class="bullets">
          <li>CalciNova PX is an advanced, professional grade, plant-sourced calcium and bone building formula exclusively available through healthcare professionals.</li>
          <li>The highly specialized plant calcium in CalciNova PX is micronized to ensure optimal absorption by delivering the perfect particle size.</li>
        </ul>
        <p style="font-size:9px;margin-top:6px;line-height:1.3">While your physicians are adding<br><b>YEARS TO YOUR LIFE,</b></p>
        <p style="font-size:9px;margin-top:4px;line-height:1.3">we at Veridane Wellness<br><b>ARE ADDING<br>LIFE TO YOUR YEARS</b></p>
      </div>
    </article>
  </section>
</main>
</body>
</html>
```